Bref créative
Brochure for Professional Services Firm
Brightfen Partners
We need a great design for a brochure to be used as marketing collateral at tradeshows and for general marketing purposes. Our website is brightfenpartners.example to get additional information. We generally work with oilfield service companies.
Consulting
Corporate, professional.
===========Update==========
Requirement : Trifold
Our logo files.
Here is a sample presentation we currently use to market our services.
Some stock photos we have.
stock photos.
stock photo.

```html
<!DOCTYPE html>
<html lang="en">
<head>
<meta charset="utf-8">
<title>Brightfen Partners – Trifold Brochure Outside</title>
<link rel="stylesheet" href="https://fonts.googleapis.com/css2?family=Open+Sans:wght@400;600;700&family=Cinzel:wght@400;700&display=swap">
<style>
  :root {
    --stage: #3a2e26;
    --paper: #ffffff;
    --charcoal: #3b3d40;
    --charcoal-dark: #2f3133;
    --brand-blue: #1c9ad6;
    --brand-navy: #1f3d5c;
    --text-light: #e6e8ea;
    --text-muted: #b9bdc1;
    --photo-blue: #5b8fc6;
    --photo-blue-soft: #7fa8d2;
    --photo-grey: #d6dade;
    --photo-grey-soft: #e4e7ea;
  }
  * { box-sizing: border-box; margin: 0; padding: 0; }
  html, body { width: 1200px; height: 698px; overflow: hidden; }
  body {
    background: var(--stage);
    font-family: "Open Sans", Arial, sans-serif;
    position: relative;
  }
  .trifold {
    position: absolute;
    left: 160px; top: 21px;
    width: 880px; height: 656px;
    background: var(--paper);
    display: grid;
    grid-template-columns: repeat(3, 1fr);
    grid-template-rows: 150px 28px 290px 1fr;
    box-shadow: 0 6px 18px rgba(0,0,0,.45);
  }
  .photo { display: block; width: 100%; height: 100%; }
  .pumpjack-photo {
    grid-column: 1; grid-row: 1;
    background: linear-gradient(180deg, var(--photo-blue-soft), var(--photo-blue));
  }
  .team-photo {
    grid-column: 2; grid-row: 1;
    background: linear-gradient(180deg, var(--photo-grey-soft), var(--photo-grey));
  }
  .cover-logo {
    grid-column: 3; grid-row: 1;
    display: flex; align-items: center; justify-content: center; gap: 8px;
    white-space: nowrap;
  }
  .logo-mark { width: 14px; height: 14px; background: var(--brand-blue); flex: none; }
  .logo-name {
    font-weight: 700; color: var(--brand-navy);
    font-size: 17px; letter-spacing: 1px; text-transform: uppercase;
    line-height: 1; white-space: nowrap;
  }
  .web-strip {
    grid-column: 2 / 4; grid-row: 2;
    display: flex; align-items: center; justify-content: flex-end;
    padding-right: 22px;
    border-top: 3px solid var(--brand-blue);
  }
  .web-strip .url { color: var(--brand-blue); font-size: 12px; font-weight: 600; }
  .rig-photo {
    grid-column: 2 / 4; grid-row: 3;
    background: linear-gradient(180deg, var(--photo-blue), var(--photo-blue-soft));
  }
  .about {
    grid-column: 1; grid-row: 2 / 5;
    background: var(--charcoal);
    padding: 16px 20px 22px;
    color: var(--text-light);
    position: relative;
  }
  .about::after {
    content: ""; position: absolute; left: 0; right: 0; bottom: 0;
    height: 10px; background: var(--brand-blue);
  }
  .about-heading {
    display: flex; align-items: center; gap: 8px;
    font-size: 15px; font-weight: 700; margin-bottom: 10px;
  }
  .about-heading svg { flex: none; }
  .about-intro { color: var(--brand-blue); font-size: 10.5px; font-weight: 600; line-height: 1.5; margin-bottom: 10px; }
  .about p.body { font-size: 9.5px; line-height: 1.6; color: var(--text-muted); margin-bottom: 10px; }
  .back-panel {
    grid-column: 2; grid-row: 4;
    display: flex; flex-direction: column; align-items: center; justify-content: center;
    gap: 12px; text-align: center;
  }
  .back-panel .logo-name { font-size: 15px; }
  .address { font-size: 9.5px; line-height: 1.6; color: #55595d; font-style: normal; }
  .address strong { color: var(--brand-navy); }
  .back-panel .url { font-size: 10px; color: var(--brand-blue); font-weight: 600; }
  .slogan-panel {
    grid-column: 3; grid-row: 4;
    background: var(--charcoal-dark);
    color: var(--paper);
    font-family: "Cinzel", Georgia, serif;
    display: flex; flex-direction: column; justify-content: center;
    padding-left: 30px; line-height: 1.15;
  }
  .slogan-panel .line1 { font-size: 17px; }
  .slogan-panel .line2 { font-size: 25px; font-weight: 700; }
  .slogan-panel .line2 small { font-size: 16px; font-weight: 400; }
  .slogan-panel .line3 { font-size: 17px; padding-left: 70px; }
</style>
</head>
<body>
  <main class="trifold">
    <div class="photo pumpjack-photo" role="img" aria-label="Photo of an oilfield pumpjack on open land"></div>
    <div class="photo team-photo" role="img" aria-label="Photo of consultants meeting with a client"></div>
    <div class="cover-logo">
      <span class="logo-mark"></span>
      <span class="logo-name">Brightfen Partners</span>
    </div>

    <section class="about">
      <h2 class="about-heading">
        <svg width="16" height="16" viewBox="0 0 16 16" aria-hidden="true"><circle cx="8" cy="8" r="7" fill="var(--brand-blue)"/><rect x="7" y="7" width="2" height="5" fill="#fff"/><rect x="7" y="4" width="2" height="2" fill="#fff"/></svg>
        About Us
      </h2>
      <p class="about-intro">We are driven by results, built on trust and devoted to every client we serve.</p>
      <p class="body">Brightfen Partners is a consulting firm that helps oilfield service companies grow. We combine field experience with sound financial thinking to guide owners through change.</p>
      <p class="body">Our team works beside yours on strategy, operations and growth planning. Every engagement starts with listening, so the plan we build fits the way you really work.</p>
      <p class="body">From acquisitions and valuations to process reviews and leadership coaching, we deliver clear advice and practical steps that your people can carry forward with confidence.</p>
      <p class="body">We measure our success by yours. Long relationships, honest counsel and steady results are what our clients value most.</p>
    </section>

    <div class="web-strip"><span class="url">www.brightfenpartners.example</span></div>
    <div class="photo rig-photo" role="img" aria-label="Photo of oil rig wellhead equipment against the sky"></div>

    <section class="back-panel">
      <div class="cover-logo">
        <span class="logo-mark" style="width:12px;height:12px"></span>
        <span class="logo-name">Brightfen Partners</span>
      </div>
      <address class="address">
        1234 Example Road, Suite 100<br>
        Northfield, TX 75000<br>
        <strong>Phone:</strong> 555-0100<br>
        <strong>Email:</strong> info@brightfenpartners.example
      </address>
      <span class="url">www.brightfenpartners.example</span>
    </section>

    <section class="slogan-panel">
      <span class="line1">Your Company</span>
      <span class="line2">SLOGAN <small>will be</small></span>
      <span class="line3">come here</span>
    </section>
  </main>
</body>
</html>
```